Mental Health

QRT HAVEN
Behavioral Health
4172 W. Pell St. Mesa, AZ 85219
Gwendolyn (480)555-0142 / Omar 480-555-0187

Email: QRTHaven@Mailvex.example
Newly Remodeled & Spacious
g Staff
Registered Nurses
Licensed Independent &
Professional Substance &
Abuse Counselors
Behavioral Health Techs
Certified Caregivers
Behavioral Health &
Substance Abuse Professionals

To Refer a Patient
About Us
QRT Haven is a Fully Staffed Behavioral
Health Residential Facility, providing
treatment plans for adults suffering
with various Behavioral Health and
Substance Abuse disorders, while living
in a nice safe, clean and supportive
environment. Our home offers clients the
ability to learn the necessary skills to
help clients adapt, build self confidence
as well as independence, with the goal
of reducing the probability of a future
crisis or possible relapse. We offer
counseling programs, consisting of a
variety of addiction and recovery support
groups, independent living, coping and
social skills groups, as well as assisting
clients with using tools to create a resume
to help obtain employment and so much
more. We are committed to teaching
self management care and allowing
clients to understand how to utilize the
resources, skills and tools available for
long term success by providing superior
quality, all-inclusive living arrangements
and treatment options.

Thank you for your patience while I update the final content needed for us to make the final decision this week.

```html
<!DOCTYPE html>
<html lang="en">
<head>
<meta charset="utf-8">
<title>QRT Haven Business Card</title>
<link rel="stylesheet" href="https://fonts.googleapis.com/css2?family=Arimo:wght@400;700&family=Open+Sans:wght@600&display=swap">
<style>
  :root {
    --board: #2a2a2a;
    --paper: #ffffff;
    --brand-blue: #0a6bb8;
    --brand-green: #7ab62f;
    --ink: #3a3a3a;
    --faint: rgba(255,255,255,0.08);
  }
  * { box-sizing: border-box; margin: 0; padding: 0; }
  html, body { width: 1075px; height: 1200px; overflow: hidden; background: var(--board); }
  body { position: relative; font-family: "Arimo", Arial, sans-serif; }

  .card {
    position: absolute; left: 206px; width: 663px; height: 395px;
    overflow: hidden; box-shadow: 3px 3px 4px rgba(0,0,0,0.6);
  }
  .card--front { top: 187px; background: var(--paper); }
  .card--back { top: 637px; background: var(--brand-blue); }

  .wordmark { position: absolute; left: 37px; display: flex; align-items: center; gap: 14px; }
  .card--front .wordmark { top: 93px; }
  .card--back .wordmark { top: 95px; }
  .wordmark__dot { width: 62px; height: 62px; border-radius: 50%; background: var(--brand-green); }
  .card--back .wordmark__dot { background: var(--paper); }
  .wordmark__name { font-size: 50px; font-weight: 400; color: var(--brand-blue); letter-spacing: 1px; }
  .card--back .wordmark__name { color: var(--paper); }

  .contacts { position: absolute; right: 43px; top: 44px; text-align: right; }
  .contact__name { font-family: "Open Sans", Arial, sans-serif; font-weight: 600; font-size: 25px; line-height: 28px; color: var(--brand-blue); }
  .contact__phone { font-size: 18px; line-height: 22px; color: var(--ink); margin-bottom: 10px; }
  .contact__label { color: var(--brand-green); font-weight: 700; }

  .waves { position: absolute; left: 0; top: 0; width: 663px; height: 395px; }

  .company { position: absolute; right: 46px; top: 258px; text-align: right; color: var(--paper); font-size: 18px; line-height: 23.5px; }
  .company__email { margin-bottom: 22px; }
  .company__name { font-weight: 700; }

  .deco-ring { position: absolute; left: 248px; top: -53px; width: 414px; height: 414px; border-radius: 50%; background: var(--faint); }

  .services { position: absolute; top: 244px; list-style: none; color: var(--paper); font-size: 18px; line-height: 23.4px; }
  .services--left { left: 38px; }
  .services--right { left: 343px; }
  .services li::before { content: "\25CF"; font-size: 12px; margin-right: 6px; vertical-align: 2px; }
</style>
</head>
<body>

<section class="card card--front">
  <svg class="waves" viewBox="0 0 738 439" preserveAspectRatio="none" aria-hidden="true">
    <path fill="var(--brand-blue)" d="M0,345 C150,405 300,375 430,292 C540,228 640,210 738,238 V439 H0 Z"/>
    <path fill="none" stroke="var(--paper)" stroke-width="7" d="M70,405 C240,408 370,330 470,265 C560,210 620,200 660,200"/>
    <path fill="var(--brand-blue)" d="M90,400 C250,405 380,325 480,258 C560,208 610,198 646,200 C590,206 530,226 450,280 C350,345 220,392 90,400 Z"/>
    <path fill="var(--brand-green)" d="M0,308 C110,355 240,348 345,273 C250,340 120,370 0,342 Z"/>
  </svg>

  <div class="wordmark">
    <span class="wordmark__dot"></span>
    <span class="wordmark__name">QRT Haven</span>
  </div>

  <div class="contacts">
    <p class="contact__name">GWENDOLYN</p>
    <p class="contact__phone"><span class="contact__label">P:</span> (480)555-0142</p>
    <p class="contact__name">OMAR</p>
    <p class="contact__phone"><span class="contact__label">P:</span> 480-555-0187</p>
  </div>

  <div class="company">
    <p class="company__email">QRTHaven@Mailvex.example</p>
    <p class="company__name">QRT HAVEN</p>
    <p>Behavioral Health</p>
    <p>4172 W. Pell St. Mesa, AZ 85219</p>
  </div>
</section>

<section class="card card--back">
  <div class="deco-ring"></div>

  <div class="wordmark">
    <span class="wordmark__dot"></span>
    <span class="wordmark__name">QRT Haven</span>
  </div>

  <ul class="services services--left">
    <li>Newly Remodeled &amp; Spacious</li>
    <li>General Staff</li>
    <li>Registered Nurses</li>
    <li>Licensed Independent</li>
    <li>Professional Substance</li>
  </ul>
  <ul class="services services--right">
    <li>Abuse Counselors</li>
    <li>Behavioral Health Techs</li>
    <li>Certified Caregivers</li>
    <li>Behavioral Health</li>
    <li>Substance Abuse Professionals</li>
  </ul>
</section>

</body>
</html>
```